依頼詳細
請求書等の書類を郵送するための封筒のデザインをお願いしたいと思っております。
イメージは長3封筒窓なしの片側に透明感のあるグレーでHISAGOTECHWORKSと入れてほしいです。
きっちり入れるのではなくて、文字が封筒からはみ出した感じでもいいです。
あと、SDGsのロゴを入れてほしいです。
記載項目
表面;株式会社ヒサゴテックワークス 〒668-0931 兵庫県宝塚市柚ノ木町8番37号(事務所)柚ノ木町9番24号(資材倉庫)TEL.0797-58-2916 FAX.0797-36-1729 Mobile.090-6142-9358 e-mail. info@hisago-kenso.co.jp URL.https://www.hisago-kenso.co.jp SDGsロゴに関しては17項目ではなく丸のロゴの横に会社ロゴを入れて下に 弊社は持続可能な開発目標(SDGs)を支援しています  と入れてほしいです。
希望イメージ
シンプル 複雑
単色 カラフル
暗い 明るい
日常 高級
遊び心 厳粛
未来的 伝統的
女性的 男性的
希望する色
青系、水色系、無彩色系
納品ファイル
補足説明
事業内容を入れてほしいです。各種防水工事、シーリング工事、外壁塗装工事、その他 を何処かにつけてください。よろしくお願いします。
ロゴとSDGsのロゴは大きくなくて良いです。あと会社ロゴとSDGsのロゴの間に黒の棒線がひつようです。SDGsの詳細をご覧いただけるとわかります。よろしくお願いします。
沢山の提案ありがとうございます。社内で話し合いご返事させて頂きます。

※封筒のサイズを変更いたします。長形3号封筒からA4が入る角形2号に変更したいので、宜しくお願い致します。
仕事が忙しい為、選定する時間が取れません。何卒ご了承ください。

ご提案ありがとうございました。
シンプルにデザインが気に入ったので決めました。

沢山の提案ありがとうございました。

```html
<!DOCTYPE html>
<html lang="ja">
<head>
<meta charset="utf-8">
<title>ヒサゴテックワークス 角形2号封筒</title>
<link href="https://fonts.googleapis.com/css2?family=Montserrat:wght@800&family=Noto+Sans+JP:wght@400;700&display=swap" rel="stylesheet">
<style>
  :root{
    --stage:#e9eaeb;
    --paper:#ffffff;
    --flap:#3b86c6;
    --flap-edge:#5b9bd1;
    --ghost:#e3e4e6;
    --ink:#2b2b2b;
    --ink-soft:#555;
    --rule:#1a1a1a;
    --badge:#9aa7b4;
  }
  html,body{margin:0;padding:0;width:882px;height:1200px;overflow:hidden;background:var(--stage);}
  .canvas{position:relative;width:882px;height:1200px;}
  .envelope{position:absolute;left:82px;top:49px;width:718px;height:1095px;background:var(--paper);box-shadow:0 1px 3px rgba(0,0,0,.12);overflow:hidden;}
  .flap{position:absolute;left:0;top:0;width:718px;height:100px;}
  .flap-name{position:absolute;left:0;right:0;top:28px;text-align:center;color:#fff;font:700 15px 'Noto Sans JP',sans-serif;letter-spacing:.08em;}
  .flap-name .dot{display:inline-block;width:9px;height:9px;border-radius:50%;background:#fff;margin-right:6px;vertical-align:1px;}
  .ghost-name{position:absolute;left:0;top:0;}
  .ghost-name text{font:800 74px 'Montserrat',sans-serif;fill:var(--ghost);}
  .sdgs-note{position:absolute;left:190px;top:183px;font:400 9px 'Noto Sans JP',sans-serif;color:var(--ink-soft);letter-spacing:.02em;}
  .marks{position:absolute;left:78px;top:790px;display:flex;align-items:center;height:100px;}
  .brand{display:flex;align-items:center;gap:8px;font:700 17px 'Noto Sans JP',sans-serif;color:var(--flap);width:170px;}
  .brand .dot{width:14px;height:14px;border-radius:50%;background:var(--flap);flex:none;}
  .divider{width:2px;height:96px;background:var(--rule);margin:0 26px 0 6px;}
  .badge{width:96px;height:96px;border-radius:50%;background:var(--badge);}
  .contact{position:absolute;left:78px;top:905px;font-family:'Noto Sans JP',sans-serif;color:var(--ink);}
  .contact .company{font-weight:700;font-size:13px;margin:0 0 4px;}
  .contact .line{font-size:10px;line-height:15px;margin:0;}
  .contact .row{display:flex;gap:26px;font-size:10px;line-height:16px;margin-top:4px;}
  .contact .row span{display:flex;align-items:center;gap:4px;}
  .contact svg{width:10px;height:10px;fill:var(--ink-soft);}
</style>
</head>
<body>
<div class="canvas">
  <div class="envelope">
    <svg class="flap" viewBox="0 0 718 100" aria-hidden="true">
      <polygon points="0,0 718,0 718,88 700,100 18,100 0,88" fill="var(--flap)"/>
      <line x1="0" y1="88" x2="18" y2="100" stroke="var(--flap-edge)" stroke-width="1"/>
      <line x1="718" y1="88" x2="700" y2="100" stroke="var(--flap-edge)" stroke-width="1"/>
    </svg>
    <div class="flap-name"><span class="dot"></span>HISAGO TECH WORKS</div>

    <svg class="ghost-name" width="120" height="1095" viewBox="0 0 120 1095" aria-hidden="true">
      <text transform="translate(60 1085) rotate(-90)" textLength="920" lengthAdjust="spacingAndGlyphs">HISAGOTECHWORKS</text>
    </svg>

    <p class="sdgs-note">弊社は持続可能な開発目標(SDGs)を支援しています</p>

    <div class="marks">
      <div class="brand"><span class="dot"></span>HisagoTech</div>
      <div class="divider"></div>
      <div class="badge" role="img" aria-label="SDGs支援マーク"></div>
    </div>

    <div class="contact">
      <p class="company">株式会社ヒサゴテックワークス</p>
      <p class="line">〒668-0931 兵庫県宝塚市柚ノ木町8番37号（事務所）／兵庫県宝塚市柚ノ木町9番24号（資材倉庫）</p>
      <p class="line">TEL.0797-58-2916　FAX.0797-36-1729</p>
      <div class="row">
        <span><svg viewBox="0 0 10 10"><rect x="2.5" y="0.5" width="5" height="9" rx="1"/></svg>090-6142-9358</span>
        <span><svg viewBox="0 0 10 10"><rect x="0.5" y="2" width="9" height="6" rx="0.8"/></svg>info@hisago-kenso.co.jp</span>
        <span><svg viewBox="0 0 10 10"><circle cx="5" cy="5" r="4.5"/></svg>https://www.hisago-kenso.co.jp</span>
      </div>
    </div>
  </div>
</div>
</body>
</html>
```